PowerPoint Design for a Biotech Consulting Firm

We need a powerpoint design for a new business based in Philadelphia called VentoraRx. This is a consulting firm that will serve medical diagnostics industry, which is part of the life science/healthcare industry focusing on developing and marketing products that help in early detection, monitoring or management of diseases. Our consulting firm will help medical diagnostic companies to overcome key challenges in designing, evaluating and marketing new products.Our company name is VentoraRx. Ventora is Latin word for "something", Dx represents diagnostics. The idea behind the name is that we help companies to transform the original, early product ideas ("nothing") into "something" which is a product with full clinical utility that will help to improve health and well-being.The powerpoint should use the visual feel of the logo (attached), be modern, simple and clean looking and represent creativity, innovation, scientific thinking and progress.

Target Market(s)

Biotech

Industry/Entity Type

Biotechnology

Font styles to use
Sans Serif

Colors
0355a3
3276b5
85abd2
cfdeed
ffffff
959595
aaaaaa
cbcbcb
070707

Requirements
Must have
• - look and feel, logo colors
• - multiple slide formats

```html
<!DOCTYPE html>
<html lang="en">
<head>
<meta charset="utf-8">
<title>VentoraRx – Presentation Slides</title>
<link href="https://fonts.googleapis.com/css2?family=Hind:wght@400;500;600&display=swap" rel="stylesheet">
<style>
:root{
  --navy:#0355a3;
  --blue:#3276b5;
  --accent:#1f7ae0;
  --sky:#85abd2;
  --mist:#cfdeed;
  --white:#ffffff;
  --grey:#959595;
  --grey-2:#aaaaaa;
  --grey-3:#cbcbcb;
  --ink:#070707;
  --stage:#eef2f7;
}
*{box-sizing:border-box;margin:0;padding:0}
html,body{width:998px;height:1200px;overflow:hidden}
body{background:var(--stage);font-family:"Hind",sans-serif;color:var(--ink);position:relative}
.slide{position:absolute;width:311px;height:176px;background:var(--white);overflow:hidden;box-shadow:0 2px 6px rgba(0,0,0,.18)}
.slide.cover{width:522px;height:294px}
.abs{position:absolute}
.ph{position:absolute}
.ph-tubes{background:linear-gradient(160deg,#e6eef6 0%,#39a9e4 45%,#1b6fb8 100%)}
.ph-lab{background:linear-gradient(135deg,#f1f4f7 0%,#b9d3ea 50%,#2b8fd6 100%)}
.ph-flasks{background:radial-gradient(circle at 45% 45%,#2d7fd0 0%,#7a3f73 35%,#c46a2e 55%,#0b0b10 80%)}
.ph-chart{background:linear-gradient(150deg,#e9f1f9 0%,#9cc3e8 55%,#2f7fd2 100%)}
.ph-dish{background:linear-gradient(160deg,#eef0f0 0%,#cfd3d3 55%,#b4a594 100%)}
.ph-mask{background:linear-gradient(160deg,#e2e6ea 0%,#a9b6c0 50%,#4f8c7c 100%)}
.title{font-weight:500;line-height:1.15;font-size:14px}
.title .hl{color:var(--accent)}
.body{font-size:4.2px;line-height:1.75;color:#555;text-align:justify}
.mark{position:absolute;font-size:6px;font-weight:500;color:var(--ink);letter-spacing:.1px}
.foot{position:absolute;left:0;right:0;bottom:0;height:4px;background:var(--accent)}
.foot::before{content:"";position:absolute;left:0;top:0;bottom:0;width:32%;background:var(--ink)}
.pg{position:absolute;left:8px;bottom:0;font-size:3px;color:#fff;z-index:1;line-height:4px}
.tile{position:absolute;display:flex;align-items:center;justify-content:center;text-align:center;font-size:3.4px;font-weight:600;letter-spacing:.6px;color:#fff;line-height:1.3}
.label{font-size:3.6px;letter-spacing:1px;color:var(--accent);font-weight:500}
.note{font-size:3.6px;line-height:1.5;color:#555}
.vert{writing-mode:vertical-rl;transform:rotate(180deg);font-weight:500;letter-spacing:1px;line-height:1}
.brand{position:absolute;left:727px;top:88px;width:230px;font-size:40px;font-weight:500;color:var(--ink)}
</style>
</head>
<body>

<!-- Cover slide -->
<section class="slide cover" style="left:60px;top:66px">
  <div class="abs" style="left:288px;top:0;width:234px;height:294px;background:var(--blue)"></div>
  <div class="ph ph-lab" style="left:207px;top:0;width:162px;height:136px" role="img" aria-label="Scientist in gloves handling a flask next to a microscope"></div>
  <div class="ph ph-tubes" style="left:10px;top:81px;width:188px;height:188px" role="img" aria-label="Rack of test tubes with blue liquid"></div>
  <div class="abs" style="left:90px;top:14px;font-size:44px;font-weight:500;color:var(--accent);line-height:1">02</div>
  <div class="abs" style="left:171px;top:24px;font-size:13px;font-weight:500;color:var(--accent);letter-spacing:1.5px;line-height:1.2">Product<br>Title</div>
  <div class="abs vert" style="left:183px;top:166px;font-size:12px;color:var(--ink);height:64px">Product</div>
  <div class="abs vert" style="left:198px;top:180px;font-size:12px;color:var(--ink);height:48px">Title</div>
  <div class="abs" style="left:173px;top:233px;font-size:44px;font-weight:600;color:var(--ink);line-height:1">01</div>
  <div class="abs vert" style="left:417px;top:78px;font-size:12px;color:var(--white);height:64px">Product</div>
  <div class="abs vert" style="left:432px;top:92px;font-size:12px;color:var(--white);height:48px">Title</div>
  <div class="ph ph-mask" style="left:324px;top:158px;width:162px;height:136px" role="img" aria-label="Researcher in a mask using a pipette over a green flask"></div>
  <div class="abs" style="left:408px;top:146px;font-size:44px;font-weight:600;color:var(--white);line-height:1">03</div>
  <div class="abs" style="left:0;top:286px;width:100px;height:6px;background:var(--ink)"></div>
  <div class="abs" style="left:165px;top:286px;width:123px;height:6px;background:var(--accent)"></div>
  <div class="abs" style="left:20px;top:286px;font-size:4px;color:#fff;line-height:6px">21</div>
</section>

<!-- Brand name -->
<div class="brand">VentoraRx</div>

<!-- Our New Products -->
<section class="slide" style="left:670px;top:212px">
  <div class="mark" style="left:272px;top:16px">VentoraRx</div>
  <div class="title abs" style="left:27px;top:28px"><span class="hl">Our New</span><br>Products</div>
  <p class="body abs" style="left:123px;top:30px;width:140px">Our consulting team helps diagnostic companies shape, test and launch new products with strong clinical value and a clear path to market.</p>
  <div class="ph ph-chart" style="left:0;top:87px;width:44px;height:44px" role="img" aria-label="Lab data chart"></div>
  <div class="ph ph-dish" style="left:44px;top:87px;width:44px;height:44px" role="img" aria-label="Pipette over a petri dish"></div>
  <div class="tile" style="left:88px;top:87px;width:45px;height:44px;background:var(--blue)">WRITE HERE<br>SOMETHING</div>
  <div class="ph ph-tubes" style="left:133px;top:87px;width:44px;height:44px" role="img" aria-label="Blue test tubes"></div>
  <div class="ph ph-lab" style="left:177px;top:87px;width:44px;height:44px" role="img" aria-label="Microscope work"></div>
  <div class="ph ph-flasks" style="left:221px;top:87px;width:45px;height:44px" role="img" aria-label="Coloured flasks"></div>
  <div class="tile" style="left:266px;top:87px;width:45px;height:44px;background:var(--mist)">WRITE HERE<br>SOMETHING</div>
  <div class="ph ph-flasks" style="left:0;top:131px;width:44px;height:45px" role="img" aria-label="Coloured flasks"></div>
  <div class="tile" style="left:44px;top:131px;width:44px;height:45px;background:var(--grey)">WRITE HERE<br>SOMETHING</div>
  <div class="ph ph-chart" style="left:88px;top:131px;width:45px;height:45px" role="img" aria-label="Lab data chart"></div>
  <div class="ph ph-mask" style="left:133px;top:131px;width:44px;height:45px" role="img" aria-label="Researcher with a flask"></div>
  <div class="tile" style="left:177px;top:131px;width:44px;height:45px;background:var(--sky)">WRITE HERE<br>SOMETHING</div>
  <div class="ph ph-lab" style="left:221px;top:131px;width:45px;height:45px" role="img" aria-label="Blue liquid in a flask"></div>
  <div class="ph ph-dish" style="left:266px;top:131px;width:45px;height:45px" role="img" aria-label="Microscope on a bench"></div>
</section>

<!-- Our Awesome Products -->
<section class="slide" style="left:670px;top:407px">
  <div class="mark" style="left:12px;top:16px">VentoraRx</div>
  <div class="title abs" style="left:44px;top:38px"><span class="hl">Our Awesome</span><br>Products</div>
  <p class="body abs" style="left:48px;top:84px;width:66px">A company is an association or collection of individuals, whether natural persons, legal persons, or a mixture of both. A company is an association or collection of individuals, whether natural persons, legal persons, or a mixture of both.</p>
  <div class="ph ph-dish" style="left:158px;top:0;width:73px;height:108px" role="img" aria-label="Pipette dropping blue liquid into a petri dish"></div>
  <div class="ph ph-chart" style="left:239px;top:26px;width:72px;height:108px" role="img" aria-label="Blue flask over a printed chart"></div>
  <div class="ph ph-flasks" style="left:121px;top:115px;width:110px;height:39px" role="img" aria-label="Coloured flasks on black"></div>
  <div class="foot"></div><span class="pg">16</span>
</section>

<!-- Your Title -->
<section class="slide" style="left:11px;top:600px">
  <div class="mark" style="left:276px;top:16px">VentoraRx</div>
  <div class="title abs" style="left:27px;top:24px">Your <span class="hl">Title</span></div>
  <p class="body abs" style="left:27px;top:44px;width:84px">Our consulting team helps diagnostic companies shape, test and launch new products with strong clinical value and a clear path to market.</p>
  <div class="ph ph-flasks" style="left:137px;top:42px;width:135px;height:115px" role="img" aria-label="Coloured laboratory flasks on a black background"></div>
  <div class="foot"></div><span class="pg">17</span>
</section>

<!-- Product & Details -->
<section class="slide" style="left:340px;top:600px">
  <div class="ph ph-chart" style="left:0;top:0;width:78px;height:86px" role="img" aria-label="Blue flask over a chart"></div>
  <div class="ph ph-dish" style="left:82px;top:0;width:77px;height:86px" role="img" aria-label="Pipette over a petri dish"></div>
  <div class="ph ph-flasks" style="left:0;top:89px;width:78px;height:87px" role="img" aria-label="Coloured flasks"></div>
  <div class="ph ph-mask" style="left:82px;top:89px;width:77px;height:87px" role="img" aria-label="Researcher with a green flask"></div>
  <div class="mark" style="left:276px;top:16px">VentoraRx</div>
  <div class="title abs" style="left:170px;top:28px"><span class="hl">Product</span><br>&amp; Details</div>
  <p class="body abs" style="left:170px;top:66px;width:134px">Our consulting team helps diagnostic companies shape, test and launch new products with strong clinical value and a clear path to market.</p>
  <div class="abs" style="left:159px;right:0;bottom:0;height:4px;background:var(--accent)"></div>
</section>

<!-- Products & Details -->
<section class="slide" style="left:670px;top:600px">
  <div class="mark" style="left:12px;top:16px">VentoraRx</div>
  <div class="title abs" style="left:24px;top:40px"><span class="hl">Products</span><br>&amp; Details</div>
  <p class="body abs" style="left:24px;top:80px;width:118px">Our consulting team helps diagnostic companies shape, test and launch new products with strong clinical value and a clear path to market.</p>
  <div class="ph ph-mask" style="left:153px;top:0;width:78px;height:85px" role="img" aria-label="Researcher with a green flask"></div>
  <div class="ph ph-chart" style="left:234px;top:0;width:77px;height:85px" role="img" aria-label="Blue flask over a chart"></div>
  <div class="ph ph-flasks" style="left:153px;top:88px;width:78px;height:88px" role="img" aria-label="Coloured flasks"></div>
  <div class="ph ph-dish" style="left:234px;top:88px;width:77px;height:88px" role="img" aria-label="Pipette over a petri dish"></div>
  <div class="abs" style="left:0;width:153px;bottom:0;height:4px;background:var(--accent)"></div>
  <div class="abs" style="left:0;width:50px;bottom:0;height:4px;background:var(--ink)"></div>
</section>

<!-- Our Latest Products -->
<section class="slide" style="left:11px;top:795px">
  <div class="ph ph-dish" style="left:0;top:0;width:63px;height:85px" role="img" aria-label="Pipette over a petri dish"></div>
  <div class="ph ph-lab" style="left:66px;top:0;width:62px;height:63px" role="img" aria-label="Microscope work"></div>
  <div class="ph ph-mask" style="left:131px;top:0;width:60px;height:118px" role="img" aria-label="Researcher with a green flask"></div>
  <div class="ph ph-flasks" style="left:0;top:88px;width:63px;height:88px" role="img" aria-label="Coloured flasks"></div>
  <div class="ph ph-chart" style="left:66px;top:66px;width:62px;height:110px" role="img" aria-label="Blue flask over a chart"></div>
  <div class="ph ph-tubes" style="left:131px;top:121px;width:60px;height:55px" role="img" aria-label="Blue test tubes"></div>
  <div class="mark" style="left:276px;top:16px">VentoraRx</div>
  <div class="title abs" style="left:204px;top:42px"><span class="hl">Our Latest</span><br>Products</div>
  <p class="body abs" style="left:204px;top:74px;width:94px;text-align:left">Our consulting team helps diagnostic companies shape, test and launch new products with strong clinical value and a clear path to market.</p>
  <div class="abs" style="left:191px;right:0;bottom:0;height:4px;background:var(--accent)"></div>
</section>

<!-- Stats & Reports: vertical bars -->
<section class="slide" style="left:340px;top:795px">
  <div class="mark" style="left:276px;top:16px">VentoraRx</div>
  <div class="title abs hl" style="left:32px;top:26px;color:var(--accent);line-height:1.5">stats &amp;<br>reports</div>
  <p class="body abs" style="left:139px;top:40px;width:156px;text-align:left">Our consulting team helps diagnostic companies shape, test and launch new products with strong clinical value and a clear path to market.</p>
  <svg class="abs" style="left:30px;top:82px" width="10" height="70" viewBox="0 0 10 70" fill="none" stroke="#555" stroke-width=".7">
    <rect x="1" y="1" width="8" height="5.5"/><line x1="0" y1="8" x2="10" y2="8"/>
    <path d="M1 27 h2 l5 -3 v8 l-5 -3 h-2z"/>
    <path d="M5 48 l4 2 -4 2 -4 -2z"/><path d="M1 53 l4 2 4 -2"/><path d="M1 55.5 l4 2 4 -2"/>
  </svg>
  <div class="abs" style="left:47px;top:82px;width:95px"><div class="label">TITLE HERE</div><p class="note">Short note on this point for the reader.</p></div>
  <div class="abs" style="left:47px;top:107px;width:95px"><div class="label">AWESOME THING</div><p class="note">Short note on this point for the reader.</p></div>
  <div class="abs" style="left:47px;top:132px;width:95px"><div class="label">SOMETHING NEW</div><p class="note">Short note on this point for the reader.</p></div>
  <svg class="abs" style="left:155px;top:92px" width="138" height="66" viewBox="0 0 138 66">
    <g fill="var(--grey)"><rect x="6" y="12" width="3" height="48"/><rect x="41" y="28" width="3" height="32"/><rect x="76" y="22" width="3" height="38"/><rect x="111" y="6" width="3" height="54"/></g>
    <g fill="var(--navy)"><rect x="11" y="36" width="3" height="24"/><rect x="46" y="4" width="3" height="56"/><rect x="81" y="36" width="3" height="24"/><rect x="116" y="14" width="3" height="46"/></g>
    <g fill="var(--sky)"><rect x="16" y="40" width="3" height="20"/><rect x="51" y="38" width="3" height="22"/><rect x="86" y="26" width="3" height="34"/><rect x="121" y="2" width="3" height="58"/></g>
    <line x1="0" y1="60" x2="138" y2="60" stroke="var(--grey-3)" stroke-width=".5"/>
  </svg>
  <div class="foot"></div><span class="pg">36</span>
</section>

<!-- Stats & Reports: horizontal bars -->
<section class="slide" style="left:670px;top:795px">
  <div class="mark" style="left:276px;top:16px">VentoraRx</div>
  <div class="title abs" style="left:32px;top:26px;color:var(--accent);line-height:1.5">stats &amp;<br>reports</div>
  <p class="body abs" style="left:139px;top:40px;width:156px;text-align:left">Our consulting team helps diagnostic companies shape, test and launch new products with strong clinical value and a clear path to market.</p>
  <svg class="abs" style="left:32px;top:86px" width="120" height="66" viewBox="0 0 120 66">
    <g fill="var(--sky)"><rect x="0" y="0" width="115" height="2.5"/><rect x="0" y="17" width="68" height="2.5"/><rect x="0" y="34" width="45" height="2.5"/><rect x="0" y="51" width="45" height="2.5"/></g>
    <g fill="var(--navy)"><rect x="0" y="4" width="65" height="2.5"/><rect x="0" y="21" width="42" height="2.5"/><rect x="0" y="38" width="100" height="2.5"/><rect x="0" y="55" width="48" height="2.5"/></g>
    <g fill="var(--grey)"><rect x="0" y="8" width="100" height="2.5"/><rect x="0" y="25" width="80" height="2.5"/><rect x="0" y="42" width="60" height="2.5"/><rect x="0" y="59" width="98" height="2.5"/></g>
  </svg>
  <svg class="abs" style="left:172px;top:82px" width="10" height="70" viewBox="0 0 10 70" fill="none" stroke="#555" stroke-width=".7">
    <rect x="1" y="1" width="8" height="5.5"/><line x1="0" y1="8" x2="10" y2="8"/>
    <path d="M1 27 h2 l5 -3 v8 l-5 -3 h-2z"/>
    <path d="M5 48 l4 2 -4 2 -4 -2z"/><path d="M1 53 l4 2 4 -2"/><path d="M1 55.5 l4 2 4 -2"/>
  </svg>
  <div class="abs" style="left:189px;top:82px;width:100px"><div class="label">TITLE HERE</div><p class="note">Short note on this point for the reader.</p></div>
  <div class="abs" style="left:189px;top:107px;width:100px"><div class="label">AWESOME THING</div><p class="note">Short note on this point for the reader.</p></div>
  <div class="abs" style="left:189px;top:132px;width:100px"><div class="label">SOMETHING NEW</div><p class="note">Short note on this point for the reader.</p></div>
  <div class="foot"></div><span class="pg">37</span>
</section>

<!-- Stats & Reports: rings -->
<section class="slide" style="left:11px;top:990px">
  <div class="mark" style="left:276px;top:16px">VentoraRx</div>
  <div class="title abs" style="left:32px;top:26px;color:var(--accent);line-height:1.5">stats &amp;<br>reports</div>
  <p class="body abs" style="left:139px;top:40px;width:156px;text-align:left">Our consulting team helps diagnostic companies shape, test and launch new products with strong clinical value and a clear path to market.</p>
  <svg class="abs" style="left:31px;top:96px" width="46" height="46" viewBox="0 0 46 46">
    <circle cx="23" cy="23" r="21" fill="none" stroke="var(--mist)" stroke-width="1"/>
    <path d="M23 2 A21 21 0 0 1 43.5 27" fill="none" stroke="var(--grey)" stroke-width="1.4"/>
    <text x="23" y="27" text-anchor="middle" font-size="11" fill="var(--accent)" font-family="Hind,sans-serif">30</text>
  </svg>
  <div class="abs" style="left:87px;top:108px;width:60px"><div class="label">PROJECT NAME</div><p class="note">Brief note on project progress.</p></div>
  <svg class="abs" style="left:178px;top:93px" width="46" height="46" viewBox="0 0 46 46">
    <circle cx="23" cy="23" r="21" fill="none" stroke="var(--mist)" stroke-width="1"/>
    <path d="M23 2 A21 21 0 1 1 2 23" fill="none" stroke="var(--grey)" stroke-width="1.4"/>
    <text x="23" y="27" text-anchor="middle" font-size="11" fill="var(--accent)" font-family="Hind,sans-serif">90</text>
  </svg>
  <div class="abs" style="left:234px;top:105px;width:60px"><div class="label">PROJECT NAME</div><p class="note">Brief note on project progress.</p></div>
  <div class="foot"></div><span class="pg">35</span>
</section>

<!-- Flowchart -->
<section class="slide" style="left:340px;top:990px">
  <div class="mark" style="left:276px;top:16px">VentoraRx</div>
  <div class="title abs" style="left:29px;top:16px;font-size:13px"><span class="hl">Perfect</span> Flowchart three</div>
  <svg class="abs" style="left:40px;top:38px" width="240" height="80" viewBox="0 0 240 80" font-family="Hind,sans-serif">
    <g fill="#fff" stroke="var(--grey-3)" stroke-width=".6">
      <rect x="8" y="22" width="41" height="34" rx="2"/><rect x="64" y="22" width="41" height="34" rx="2"/>
      <rect x="120" y="22" width="41" height="34" rx="2"/><rect x="176" y="22" width="41" height="34" rx="2"/>
    </g>
    <rect x="13" y="48" width="31" height="9" fill="var(--grey)"/><text x="28.5" y="55" text-anchor="middle" font-size="5.5" fill="#fff">idea</text>
    <rect x="69" y="14" width="31" height="9" fill="var(--blue)"/><text x="84.5" y="21" text-anchor="middle" font-size="5.5" fill="#fff">Sketch</text>
    <rect x="125" y="48" width="31" height="9" fill="var(--sky)"/><text x="140.5" y="55" text-anchor="middle" font-size="5.5" fill="#fff">Work</text>
    <rect x="181" y="14" width="31" height="9" fill="var(--grey-2)"/><text x="196.5" y="21" text-anchor="middle" font-size="5.5" fill="#fff">Deliver</text>
    <g fill="none" stroke="var(--grey)" stroke-width=".8">
      <circle cx="28.5" cy="32" r="4"/><path d="M26.5 36 v3 h4 v-3"/>
      <rect x="192" y="30" width="9" height="2.5"/><rect x="193" y="32.5" width="7" height="6"/>
    </g>
    <path d="M80 40 l8 -8 1.5 1.5 -8 8z" fill="var(--navy)"/>
    <g stroke="var(--navy)" stroke-width="1.1"><path d="M135 30 l11 11"/><path d="M146 30 l-11 11"/></g>
    <g fill="none" stroke="var(--navy)" stroke-width="1"><path d="M84 14 C 92 -2 118 -2 126 12"/></g>
    <path d="M126 12 l-3 -1 3 4 1 -4z" fill="var(--navy)"/>
    <g fill="none" stroke="var(--grey)" stroke-width="1"><path d="M28 58 C 38 74 64 74 72 58"/></g>
    <path d="M72 58 l-3 1 4 -4 0 4z" fill="var(--grey)"/>
    <g fill="none" stroke="var(--sky)" stroke-width="1"><path d="M140 58 C 150 74 176 74 184 60"/></g>
    <path d="M184 60 l-3 1 4 -4 0 4z" fill="var(--sky)"/>
  </svg>
  <p class="note abs" style="left:22px;top:130px;width:270px;font-size:3.8px">Lorem ipsum dolor sit amet, consectetur adipiscing elit. Aliquam tincidunt ante nec sem congue convallis. Pellentesque vel mauris quis nisl ornare rutrum in id risus. Proin vehicula ut sem et tempus. Interdum et malesuada fames ac ante ipsum primis in faucibus. Pellentesque rhoncus condimentum dolor ac auctor. Vivamus viverra ornare lobortis.</p>
  <div class="foot"></div><span class="pg">29</span>
</section>

<!-- Puzzle Diagram -->
<section class="slide" style="left:670px;top:990px">
  <div class="mark" style="left:276px;top:16px">VentoraRx</div>
  <div class="title abs" style="left:26px;top:14px;font-size:13px"><span class="hl">Puzzle</span> Diagram</div>
  <svg class="abs" style="left:100px;top:38px" width="110" height="112" viewBox="0 0 110 112">
    <rect x="12" y="12" width="40" height="40" fill="var(--blue)"/><circle cx="32" cy="10" r="6" fill="var(--blue)"/>
    <rect x="54" y="12" width="40" height="40" fill="var(--mist)"/><circle cx="96" cy="32" r="6" fill="var(--mist)"/><circle cx="52" cy="32" r="6" fill="var(--blue)"/>
    <rect x="12" y="54" width="40" height="40" fill="var(--sky)"/><circle cx="10" cy="74" r="6" fill="var(--sky)"/><circle cx="32" cy="52" r="6" fill="var(--blue)"/>
    <rect x="54" y="54" width="40" height="40" fill="var(--grey)"/><circle cx="74" cy="96" r="6" fill="var(--grey)"/><circle cx="52" cy="74" r="6" fill="var(--sky)"/><circle cx="74" cy="52" r="6" fill="var(--mist)"/>
  </svg>
  <div class="abs" style="left:50px;top:62px;width:52px;text-align:right"><div class="label" style="letter-spacing:0;color:var(--navy)">ELEMENT ONE</div><p class="note">Lorem ipsum dolor sit amet, consectetur adipiscing elit. Aliquam tincidunt ante nec</p></div>
  <div class="abs" style="left:208px;top:62px;width:52px"><div class="label" style="letter-spacing:0;color:var(--mist)">ELEMENT THREE</div><p class="note">Lorem ipsum dolor sit amet, consectetur adipiscing elit. Aliquam tincidunt ante nec</p></div>
  <div class="abs" style="left:40px;top:110px;width:52px;text-align:right"><div class="label" style="letter-spacing:0;color:var(--sky)">ELEMENT TWO</div><p class="note">Lorem ipsum dolor sit amet, consectetur adipiscing elit. Aliquam tincidunt ante nec</p></div>
  <div class="abs" style="left:208px;top:103px;width:52px"><div class="label" style="letter-spacing:0;color:var(--grey)">ELEMENT FOUR</div><p class="note">Lorem ipsum dolor sit amet, consectetur adipiscing elit. Aliquam tincidunt ante nec</p></div>
  <div class="foot"></div><span class="pg">27</span>
</section>

</body>
</html>
```